Flyer for New Spa Opening

We need a flyer to increase customer's awareness of our new spa located in Yangon, Myanmar, in a middle-upper class shopping mall. A new hotel will be opening above the mall in Dec 2013.
Updates

Have made payment guaranteed.  Need a good flyer. Thanks.

Hi, I have uploaded a Words File for Flyer Text. Thanks!

Dear Designers,

I have setup a 2nd award, there's too many outstanding designs! Thanks so much.

Regards
Odile

Target Market(s)

-Hotel guest who wants to a spa session to relax
-Woman between 18 - 55 years old who have high spending power in a poor country(Myanmar). They like to use "Big Brands" but do not have much variety available in their country.

Industry/Entity Type

Shopping

Requirements
Must have
• Our services include Body Spa, Facial, Nails, Waxing & Foot Reflexology. We use well-known international brands in our spa including Veloranthe, KUV, Marven, Brenzo Lativa and TORVE.

Veloranthe, the skin care system researched and developed by The Halvering Dermal Academy (HDA), is an international leader in today’s skin care industry.

We are authorized Veloranthe skin spa to provide professional facial and retailing Veloranthe products.

Include the logo of the brands

Quellmoor Spa
add: No 82, Kelvash Road, Morrin Plaza (Level-5) (7168), Dagon Township, Yangon
tel: +959 62087315
email: contactus@vertlane-holdco.example

Nice to have
• visually nice and relaxing spa pictures.
Should not have
• price

```html
<!DOCTYPE html>
<html lang="en">
<head>
<meta charset="utf-8">
<title>Quellmoor Spa Flyer</title>
<link rel="stylesheet" href="https://fonts.googleapis.com/css2?family=Cinzel:wght@400;600&family=Great+Vibes&family=Open+Sans:ital,wght@0,600;0,700;1,700&display=swap">
<style>
:root{
  --page:#ffffff;
  --wine:#7d1414;
  --wine-deep:#5e0b0b;
  --blush:#f7d3cf;
  --blush-light:#fdeeea;
  --orange:#f0a20e;
  --orange-dark:#c9780a;
  --amber-text:#f6a623;
  --night:#1c1a10;
  --olive:#3b3a1e;
  --white:#ffffff;
  --logo-grey:#555555;
}
*{margin:0;padding:0;box-sizing:border-box}
html,body{width:1200px;height:1089px;overflow:hidden;background:var(--page)}
.canvas{position:relative;width:1200px;height:1089px}

/* Front panel */
.front{position:absolute;left:70px;top:34px;width:507px;height:1015px;overflow:hidden;
  background:linear-gradient(180deg,var(--blush-light) 0%,var(--blush) 55%,#f3b9b6 75%)}
.front .hero-photo{position:absolute;left:0;top:0;width:100%;height:290px;
  background:linear-gradient(180deg,#e9c3a6 0%,#f1d2bd 45%,#f8e4da 80%,rgba(253,238,234,0) 100%)}
.brand-title{position:absolute;left:0;top:335px;width:100%;text-align:center;
  font-family:"Great Vibes",cursive;font-weight:400;font-size:66px;color:var(--wine);line-height:1}
.title-rule{position:absolute;left:40px;top:420px;width:427px;height:2px;
  background:linear-gradient(90deg,rgba(125,20,20,0),var(--wine) 30%,var(--wine) 70%,rgba(125,20,20,0))}
.services{position:absolute;left:125px;top:435px;list-style:none}
.services li{font-family:"Cinzel",serif;font-size:27px;color:var(--wine);text-transform:uppercase;
  height:49px;line-height:49px;display:flex;align-items:center}
.services li::before{content:"";width:8px;height:8px;border-radius:50%;background:var(--wine);margin-right:22px}
.authorized{position:absolute;left:23px;top:697px;width:452px;height:34px;background:var(--white);
  font-family:"Cinzel",serif;font-size:21px;color:var(--wine-deep);text-align:center;line-height:34px;white-space:nowrap}
.front .hands-photo{position:absolute;left:0;top:731px;width:100%;height:217px;
  background:linear-gradient(180deg,#f3b9b6 0%,#e77f86 40%,#d9475a 75%,#c53144 100%)}
.contact{position:absolute;left:0;bottom:0;width:100%;height:67px;background:linear-gradient(180deg,#8c1616,var(--wine-deep));
  color:var(--white);font-family:"Open Sans",sans-serif;font-weight:600;text-align:center;padding-top:12px}
.contact-line{display:block;white-space:nowrap;font-size:11.5px;line-height:20px}
.contact-line.main{font-size:13px;line-height:22px}
.contact b{font-weight:700}

/* Back panel */
.back{position:absolute;left:622px;top:34px;width:548px;height:1015px;overflow:hidden;
  background:linear-gradient(160deg,#4a4522 0%,var(--olive) 30%,var(--night) 60%,#2a2514 100%)}
.menu-heading{position:absolute;left:50%;top:44px;transform:translateX(-50%);width:195px;height:47px;
  background:linear-gradient(180deg,#f7b52a,var(--orange-dark));border-radius:4px;
  font-family:"Open Sans",sans-serif;font-weight:700;font-size:28px;color:var(--white);text-align:center;line-height:47px}
.treatment{position:absolute;left:0;width:100%}
.treatment-bar{height:22px;background:linear-gradient(180deg,#f6b52b,var(--orange) 50%,var(--orange-dark));
  font-family:"Open Sans",sans-serif;font-weight:700;font-size:15.5px;color:var(--white);text-align:center;line-height:22px;white-space:nowrap}
.treatment p{padding:4px 66px 0;font-family:"Open Sans",sans-serif;font-style:italic;font-weight:700;
  font-size:12px;line-height:15.5px;color:var(--white);text-align:center}
.treatment .includes{color:var(--amber-text)}
.back .candle-photo{position:absolute;left:0;top:719px;width:100%;height:176px;
  background:linear-gradient(90deg,#2b2116 0%,#6b4a26 35%,#a88a3c 65%,#e8d24a 100%)}
.partners{position:absolute;left:0;top:895px;width:100%;height:120px;background:var(--white);
  font-family:"Open Sans",sans-serif;font-weight:700;color:var(--logo-grey)}
.partner{position:absolute;font-size:19px;line-height:26px;white-space:nowrap}
</style>
</head>
<body>
<div class="canvas">

  <section class="front">
    <div class="hero-photo" role="img" aria-label="Photo of a woman relaxing during a back massage"></div>
    <h1 class="brand-title">Quellmoor Spa</h1>
    <div class="title-rule"></div>
    <ul class="services">
      <li>Body Spa</li>
      <li>Facial</li>
      <li>Nails</li>
      <li>Waxing</li>
      <li>Foot Massage</li>
    </ul>
    <div class="authorized">AUTHORIZED VELORANTHE SKIN SPA</div>
    <div class="hands-photo" role="img" aria-label="Photo of manicured hands holding rose petals"></div>
    <div class="contact">
      <span class="contact-line">add: No 82, Kelvash Road, Morrin Plaza (Level-5) (7168), Dagon Township, Yangon</span>
      <span class="contact-line main"><b>tel: +959 62087315</b> &nbsp;|&nbsp; email: contactus@vertlane-holdco.example</span>
    </div>
  </section>

  <section class="back">
    <h2 class="menu-heading">Body Spa</h2>

    <div class="treatment" style="top:129px">
      <div class="treatment-bar">Quellmoor Day Spa (2.5hr)</div>
      <p>A luxurious spa experience designed for total relaxation. A delightful body scrub will leave your skin smooth to the touch, followed by a 60min Swedish Aromatherapy massage. The treatment is complete with a body wrap to nourish your skin and your head gently massaged, giving you a profound sense of pleasure and well-being.<br>
      <span class="includes">Includes: Body Scrub - 60min Swedish Aromatherapy Massage - Body Wrap with Head Massage</span></p>
    </div>

    <div class="treatment" style="top:291px">
      <div class="treatment-bar">Revitalizing Body Scrub (1hr)</div>
      <p>Your skin is polished smooth and soft to the touch followed by a luxurious body cream massaged in to hydrate the newly revealed skin.<br>
      <span class="includes">Includes: Body Scrub - Light Body Massage</span></p>
    </div>

    <div class="treatment" style="top:392px">
      <div class="treatment-bar">Pampering Body Treatment (1.5hr)</div>
      <p>An all over body treatment begins with a body scrub to exfoliate dead skin, in preparation for a body wrap that restores your skin to youthful condition. Lastly a luxurious body cream is massaged in leaving your skin beautifully radiant.<br>
      <span class="includes">Includes: Body Scrub - Body Wrap with Head Massage - Light Body Massage</span></p>
    </div>

    <div class="treatment" style="top:527px">
      <div class="treatment-bar">Foot Massage (1hr)</div>
      <p>Pamper your foot that has taken you a hundred miles. Following a foot soak and cleaning, we will begin foot massage on your foot reflex zones stimulating body energy and on your muscles to soothe tired heavy legs.<br>
      <span class="includes">Includes: Foot Soak - Foot Massage</span></p>
    </div>

    <div class="treatment" style="top:644px">
      <div class="treatment-bar">Traditional Body Massage (1.5hr)</div>
    </div>

    <div class="treatment" style="top:688px">
      <div class="treatment-bar">Swedish Aromatherapy Body Massage (1.5hr)</div>
    </div>

    <div class="candle-photo" role="img" aria-label="Photo of lit candles, spa stones and yellow orchids"></div>

    <div class="partners">
      <span class="partner" style="left:117px;top:34px">Marven</span>
      <span class="partner" style="left:215px;top:34px">Brenzo Lativa</span>
      <span class="partner" style="left:360px;top:34px">TORVE</span>
      <span class="partner" style="left:125px;top:76px">Veloranthe</span>
      <span class="partner" style="left:285px;top:74px;font-size:24px">KUV</span>
    </div>
  </section>

</div>
</body>
</html>
```